40k Ultra High Pressure Waterblasing Ad

We need 1 page flyer ad for our industry's brochure/membership directory.
We're a manufacturer & supplier for the Ultra High Pressure Waterblasting industry.
We'd like the ad to be simple and clean, highlighting some of our parts. Our dedication to our customers and affordable prices.
Some of the parts are Dorvel Mastrick Hoses, Sapphire Nozzles, Rotating Jetlance.

Our website is torvaflux.com

Requirements
Must have
• Dorvel Mastrick 40k Hose
• Sapphire Nozzles
• Rotating Jetlance
• **Update - Would like to incorporate the "iron skein logo w/ bulldog" from uploaded dorvel iron skein hose attachment. Highlighting the hose's features.
Nice to have
• Brief Bullet points or something else highlighting what we sell.
• - Pump replacement parts
• - Sapphire Nozzles
• - Rotating Jetlance
• - Fittings and adapters
• - Safety Gear
• I've uploaded past ads we've used.
Should not have
• Lots of text area

```html
<!DOCTYPE html>
<html lang="en">
<head>
<meta charset="utf-8">
<title>Torvaflux Jetting Technologies – Flyer</title>
<link href="https://fonts.googleapis.com/css2?family=Source+Sans+3:wght@400;600;700&display=swap" rel="stylesheet">
<style>
  :root{
    --navy:#0c2a44;
    --blue:#0a86f0;
    --label:#0a84f2;
    --ink:#151515;
    --paper:#ffffff;
    --stage:#e9e6e1;
    --dash:#555;
  }
  *{box-sizing:border-box;margin:0;padding:0}
  html,body{width:1200px;height:1200px;overflow:hidden;background:var(--stage);font-family:"Source Sans 3",sans-serif}
  .flyer{position:absolute;left:180px;top:11px;width:840px;height:1178px;background:var(--paper);box-shadow:0 4px 14px rgba(0,0,0,.25)}
  .abs{position:absolute}
  .header-band{left:0;top:11px;width:840px;height:150px;background:var(--navy)}
  .brand{left:0;top:11px;width:436px;height:150px;display:flex;align-items:center;justify-content:center;gap:12px;color:#fff;font-weight:600;font-size:20px}
  .brand-dot{width:30px;height:30px;border-radius:50%;background:var(--blue)}
  .hero-photo{left:436px;top:11px;width:392px;height:422px;background:linear-gradient(160deg,#6f6a60 0%,#b9ad8e 35%,#d7c84f 55%,#8b7a5c 80%,#55504a 100%)}
  .intro{left:23px;top:170px;width:398px;color:var(--ink);font-size:13.6px;line-height:18px;text-align:justify}
  .intro p{margin-bottom:16px}
  .intro .tagline{font-weight:700;font-size:15.2px;line-height:20px;margin-top:-2px}
  .rule{left:0;width:840px;height:6px;background:var(--navy)}
  .section-pill{left:206px;top:453px;width:424px;height:63px;border-radius:32px;background:var(--blue);color:#fff;font-weight:700;font-size:45px;display:flex;align-items:center;justify-content:center;letter-spacing:.3px}
  .card{border:1px dashed var(--dash);border-left-width:1px}
  .card-image{border-radius:2px}
  .card-caption{text-align:center;font-weight:600;font-size:15px;line-height:19px;color:var(--ink)}
  .card-label{background:var(--label);color:#fff;font-weight:600;font-size:15.5px;line-height:18px;text-align:center;display:flex;align-items:center;justify-content:center;padding:2px 8px}
  .footer{left:0;top:1059px;width:840px;height:119px;background:var(--navy);color:#fff;text-align:center}
  .phone{position:absolute;top:20px;left:0;width:840px;display:flex;align-items:center;justify-content:center;gap:10px;font-weight:600;font-size:31px;letter-spacing:.5px}
  .footer-note{position:absolute;top:62px;left:0;width:840px;font-weight:600;font-size:23px}
</style>
</head>
<body>
<div class="flyer">
  <div class="abs header-band"></div>
  <div class="abs brand"><span class="brand-dot"></span>Torvaflux Jetting Technologies, Inc.</div>
  <div class="abs hero-photo" role="img" aria-label="Rope-access worker in yellow protective gear waterblasting a wall"></div>

  <div class="abs intro">
    <p>Torvaflux Jetting Technologies manufactures quality waterblasting products for surface preparation contractors – we want to see our customers succeed so we guarantee our water jetting products and excellent customer service.</p>
    <p>At Torvaflux, the majority of our water jetting parts – including sapphire nozzles, high pressure hose fittings, and rotating water-jet jetlance are manufactured right here at our manufacturing facility. We are also a distributor for Dorvel Mastrick’s high pressure and ultra high pressure (UHP) Hose.</p>
    <p class="tagline">Torvaflux Jetting Technologies – We manufacture and machine a majority of our products right here at our family owned facility</p>
  </div>

  <div class="abs rule" style="top:474px"></div>
  <div class="abs rule" style="top:493px"></div>
  <div class="abs section-pill">Our Products</div>

  <!-- Row 1 -->
  <div class="abs card" style="left:8px;top:543px;width:266px;height:212px"></div>
  <div class="abs card-image" style="left:20px;top:553px;width:242px;height:102px;background:radial-gradient(ellipse at center,#3a3a3a 0%,#1e1e1e 60%,#ffffff 61%)" role="img" aria-label="Coiled black ultra high pressure hose with fitting"></div>
  <div class="abs card-caption" style="left:8px;top:662px;width:266px">15’, 40k, 5mm w/ 3/8” HP w/<br>Burst Shield</div>
  <div class="abs card-label" style="left:37px;top:703px;width:199px;height:25px">Ultra High Pressure Hose</div>

  <div class="abs card" style="left:287px;top:543px;width:263px;height:212px"></div>
  <div class="abs card-image" style="left:300px;top:580px;width:238px;height:80px;background:linear-gradient(180deg,#fff 0%,#a9a397 45%,#6d665b 70%,#fff 100%)" role="img" aria-label="Row of stainless sapphire nozzles"></div>
  <div class="abs card-label" style="left:324px;top:711px;width:200px;height:25px">1/4” Sapphire Nozzle</div>

  <div class="abs card" style="left:565px;top:543px;width:267px;height:212px"></div>
  <div class="abs card-image" style="left:585px;top:563px;width:228px;height:110px;background:linear-gradient(180deg,#fff 0%,#c9c9c9 45%,#8a8a8a 60%,#fff 100%)" role="img" aria-label="Air operated rotating jetlance gun"></div>
  <div class="abs card-label" style="left:600px;top:684px;width:200px;height:49px">4,800 RPM Air Operated<br>Rotating Jetlance</div>

  <!-- Row 2 -->
  <div class="abs card" style="left:8px;top:806px;width:266px;height:212px"></div>
  <div class="abs card-image" style="left:45px;top:823px;width:190px;height:115px;background:radial-gradient(circle at 50% 60%,#c8c6c0 0%,#9c9890 35%,#fff 70%)" role="img" aria-label="Pump replacement seals, springs and O-rings"></div>
  <div class="abs card-label" style="left:37px;top:958px;width:211px;height:30px">Pump Replacement Parts</div>

  <div class="abs card" style="left:291px;top:806px;width:259px;height:212px"></div>
  <div class="abs card-image" style="left:338px;top:816px;width:175px;height:115px;background:linear-gradient(180deg,#e8e6e2 0%,#b2ada4 50%,#8c877e 100%)" role="img" aria-label="Stainless female couplers with collars and glands"></div>
  <div class="abs card-caption" style="left:291px;top:936px;width:259px">3/8” Female Coupler w/ Collars<br>&amp; Glands</div>
  <div class="abs card-label" style="left:338px;top:976px;width:157px;height:30px">Fittings &amp; Adapters</div>

  <div class="abs card" style="left:565px;top:806px;width:267px;height:212px"></div>
  <div class="abs card-image" style="left:580px;top:814px;width:245px;height:140px;background:linear-gradient(180deg,#fff 0%,#3b3f38 30%,#262a26 70%,#fff 100%)" role="img" aria-label="Protective gloves, body armor and leg guards"></div>
  <div class="abs card-label" style="left:642px;top:965px;width:110px;height:32px">Safety Gear</div>

  <div class="abs footer">
    <div class="phone">
      <svg width="17" height="30" viewBox="0 0 17 30" aria-hidden="true"><rect x="1" y="1" width="15" height="28" rx="3" fill="#fff"/><rect x="3.5" y="5" width="10" height="15" fill="#0c2a44"/></svg>
      555-014-2290
    </div>
    <div class="footer-note">Have a question? Call Us</div>
  </div>
</div>
</body>
</html>
```